Website for company called VORENTbio

We need a website for our new company called VORENTbio which developed a platform/technology to identify antigen-specific T cells (immune cells) which can be used for cancer therapy, autoimmunity, etc.

The platform is called VORENT and is rapid, versatile, unbiased, and inexpensive.

We have a semi-final logo although we are not completely set on color and font of text (attached).

Target Market(s)

Our target audience at the moment would be potential investors and VCs. We eventually are interested in getting attention from scientists and cell/immunotherapy companies.

Industry/Entity Type

Healthcare/Technology

Coding

Coded - Design and coding required

Number of Pages Required

1 page

Colors
0094D4
00A9DD
6FCCEA
C7EBF8
E9F6FB
00AB8E
00BBA5
67D7C9
C6EFE9
E9F9F6
E54698
E96AAD
F1A4CE
F9D9EA
FCEFF6
A7469A
B969AE
D3A5CF
EDDBEB
F8F0F9
6B429C
8869AF
B7A5CE
E3DAEB
F3F0F8

Requirements
Must have
• Landing page about the company, About us page, Technology page (could be merged with company landing page), Contact us page

```html
<!DOCTYPE html>
<html lang="en">
<head>
<meta charset="utf-8">
<title>VORENTbio — Revolutionizing T Cell Detection</title>
<link href="https://fonts.googleapis.com/css2?family=Inter+Tight:ital,wght@0,400;0,600;0,700;0,800;1,400&display=swap" rel="stylesheet">
<style>
:root{
  --ink:#0b0b0b;
  --teal:#00ab8e;
  --teal-mid:#00bba5;
  --mint:#67d7c9;
  --mint-soft:#c6efe9;
  --mint-pale:#e9f9f6;
  --forest:#2f5d50;
  --paper:#ffffff;
}
*{box-sizing:border-box;margin:0;padding:0}
html,body{width:1200px;height:4048px;overflow:hidden}
body{position:relative;background:var(--paper);color:var(--ink);font-family:"Inter Tight",Arial,sans-serif}
.abs{position:absolute}
.heading{font-weight:800;letter-spacing:-1.5px;line-height:1.03;font-size:70px}
.swash{position:relative;z-index:0}
.swash::before{content:"";position:absolute;z-index:-1;background:var(--mint-soft);opacity:.9;border-radius:3px}

/* nav */
.brand{left:107px;top:64px;display:flex;align-items:center;gap:10px;color:var(--teal);font-weight:700;font-size:21px}
.brand-dot{width:16px;height:16px;border-radius:50%;background:var(--teal)}
.nav a{position:absolute;top:66px;font-size:20px;color:var(--ink);text-decoration:none}

/* hero */
.hero-art{left:107px;top:149px;width:430px;height:382px;background:linear-gradient(180deg,#bfe9e2 0%,#9fdcd1 45%,#2f5d50 100%);border-radius:180px 180px 8px 8px}
.hero-title{right:108px;top:150px;text-align:right}
.hero-text{right:108px;top:328px;width:520px;text-align:right;font-size:22px;line-height:31px}
.btn{position:absolute;top:479px;height:52px;border-radius:26px;font-weight:700;font-size:17px;display:flex;align-items:center;justify-content:center}
.btn-fill{left:669px;width:171px;background:var(--mint)}
.btn-line{left:924px;width:171px;border:3px solid var(--mint);background:var(--paper)}

/* about */
.about-band{left:0;top:674px;width:1200px;height:674px;background:var(--mint-soft)}
.about-title{left:68px;top:832px}
.about-title .swash::before{left:150px;right:-25px;top:10px;bottom:4px;background:#fff;opacity:.55}
.about-text{left:68px;top:1064px;width:400px;font-size:19.5px;line-height:27px}
.about-art{left:592px;top:765px;width:520px;height:507px;background:radial-gradient(ellipse at 50% 50%,#ffffff 55%,#e9f9f6 100%);border-radius:48% 52% 45% 55%/55% 40% 60% 45%}

/* mission */
.mission-title{left:68px;top:1463px}
.mission-text{left:577px;top:1452px;width:520px;font-size:20px;line-height:24px}
.stat{position:absolute;top:1687px;width:145px;height:176px;border:2px solid var(--ink);border-radius:12px;text-align:center}
.stat b{display:block;margin-top:56px;font-size:35px;font-weight:700}
.stat span{display:inline-block;margin-top:6px;font-size:16px;font-weight:600;position:relative;z-index:0}
.stat span::before{content:"";position:absolute;left:-6px;right:-14px;top:6px;bottom:-3px;background:var(--mint-soft);z-index:-1}

/* technology */
.tech-band{left:0;top:2023px;width:1200px;height:674px;background:var(--mint)}
.tech-title{left:68px;top:2080px}
.tech-title .swash::before{left:-12px;right:-16px;top:38px;bottom:-8px;background:#fff}
.tech-card{position:absolute;top:2217px;width:342px;height:402px;background:var(--paper);border-radius:12px;text-align:center}
.tech-card svg{position:absolute;left:149px;top:100px}
.tech-card h3{position:absolute;top:175px;width:100%;font-size:19px;font-weight:700}
.tech-card p{position:absolute;left:57px;top:222px;width:228px;text-align:left;font-size:13.5px;line-height:21px}

/* applications */
.apps-title{left:68px;top:2757px}
.apps-title .swash::before{left:-20px;right:-10px;top:-6px;bottom:0}
.apps-text{left:536px;top:2774px;width:560px;font-size:20px;line-height:24px}
.app-card{position:absolute;top:2887px;width:342px;height:417px;border:2px solid var(--ink);border-radius:12px;padding:68px 20px 0 20px}
.app-card h3{font-size:26px;font-weight:700;margin:0 0 18px 12px}
.app-card li{list-style:none;font-size:20px;line-height:31.5px}

/* contact */
.contact-band{left:0;top:3373px;width:1200px;height:675px;background:var(--mint-soft)}
.contact-card{left:41px;top:3440px;width:559px;height:293px;background:var(--paper);border-radius:14px}
.contact-title{left:74px;top:3476px}
.contact-text{left:67px;top:3570px;width:460px;font-size:21px;font-weight:700;line-height:27px}
.contact-text .swash::before{left:-2px;right:-2px;top:10px;bottom:-4px;background:var(--mint)}
.social{left:70px;top:3675px;display:flex;gap:12px}
.social i{display:block;width:24px;height:24px;border:2.5px solid var(--ink);border-radius:6px}
.social i:first-child{border-radius:50%}
.info{position:absolute;left:41px;width:559px;height:78px;border:2px solid var(--ink);border-radius:14px;display:flex;align-items:center;padding-left:26px}
.info b{font-size:19px;width:97px}
.info span{font-size:27px;font-weight:600}
.contact-art{left:726px;top:3448px;width:393px;height:448px;background:linear-gradient(135deg,#7fd9bf 0%,#5fc8a8 40%,#e9f6fb 60%,#8fb8b0 100%);border-radius:40px}
.caption{left:727px;top:3940px;width:400px;text-align:center;font-style:italic;font-size:18px;line-height:25px}
</style>
</head>
<body>

<header>
  <div class="abs brand"><span class="brand-dot"></span>VORENTbio</div>
  <nav class="nav">
    <a style="left:630px">About</a>
    <a style="left:715px">Technology</a>
    <a style="left:861px">Applications</a>
    <a style="left:1016px">Contact</a>
  </nav>
</header>

<section class="hero">
  <div class="abs hero-art" role="img" aria-label="Illustration of a woman in a teal shirt holding a tissue to her face, seated under a dark green blanket"></div>
  <h1 class="abs heading hero-title">Revolutionizing<br>T Cell Detection</h1>
  <p class="abs hero-text">VORENT platform delivers rapid, affordable, and versatile detection of antigen-specific T cells for breakthrough advances in cancer therapy and immunology research</p>
  <a class="btn btn-fill">Partner With Us</a>
  <a class="btn btn-line">Learn More</a>
</section>

<section>
  <div class="abs about-band"></div>
  <h2 class="abs heading about-title">About<br><span class="swash">VORENTbio</span></h2>
  <p class="abs about-text">We're pioneering the next generation of immunological research tools to accelerate breakthroughs in personalized medicine</p>
  <div class="abs about-art" role="img" aria-label="Illustration of a teal hand reaching toward scattered virus particles on a white brush-shaped background"></div>
</section>

<section>
  <h2 class="abs heading mission-title">Our Mission</h2>
  <p class="abs mission-text">VORENTbio is dedicated to transforming immunological research and therapeutic development through our innovative VORENT platform. We make T cell detection accessible, affordable, and actionable for researchers and clinicians worldwide.</p>
  <div class="stat" style="left:209px"><b>10x</b><span>Faster Detection</span></div>
  <div class="stat" style="left:528px"><b>50%</b><span>Cost Reduction</span></div>
  <div class="stat" style="left:847px"><b>99%</b><span>Accuracy Rate</span></div>
</section>

<section>
  <div class="abs tech-band"></div>
  <h2 class="abs heading tech-title"><span class="swash">VORENT</span> Technology Platform</h2>
  <article class="tech-card" style="left:68px">
    <svg width="70" height="44" viewBox="0 0 70 44"><circle cx="17" cy="21" r="15" fill="#ddd" stroke="#0b0b0b" stroke-width="3"/><path d="M32 22 H68" stroke="#0b0b0b" stroke-width="6" stroke-linecap="round"/></svg>
    <h3>Rapid Detection</h3>
    <p>Get results in hours, not days. Our streamlined protocol reduces time-to-insight by 90% compared to traditional methods.</p>
  </article>
  <article class="tech-card" style="left:429px">
    <svg width="50" height="50" viewBox="0 0 50 50" style="left:146px;top:97px"><circle cx="25" cy="25" r="21" fill="none" stroke="#0b0b0b" stroke-width="3"/><path d="M25 12 V25 L33 31" fill="none" stroke="#0b0b0b" stroke-width="3" stroke-linecap="round"/></svg>
    <h3>High Precision</h3>
    <p>Advanced algorithms and validated protocols ensure consistent, reproducible results with minimal false positives.</p>
  </article>
  <article class="tech-card" style="left:790px">
    <svg width="52" height="50" viewBox="0 0 52 50" style="left:145px;top:97px"><g fill="none" stroke="#0b0b0b" stroke-width="2.5"><ellipse cx="26" cy="25" rx="23" ry="9"/><ellipse cx="26" cy="25" rx="23" ry="9" transform="rotate(60 26 25)"/><ellipse cx="26" cy="25" rx="23" ry="9" transform="rotate(120 26 25)"/></g><circle cx="26" cy="25" r="4" fill="#0b0b0b"/></svg>
    <h3>Versatile Platform</h3>
    <p>Adaptable to multiple sample types and research applications, from basic research to clinical diagnostics.</p>
  </article>
</section>

<section>
  <h2 class="abs heading apps-title"><span class="swash">Applications</span></h2>
  <p class="abs apps-text">VORENT technology enables breakthrough discoveries across multiple therapeutic and research areas</p>
  <article class="app-card" style="left:68px">
    <h3>Oncology</h3>
    <ul><li>• Tumor-infiltrating lymphocyte analysis</li><li>• CAR-T cell therapy monitoring</li><li>• Immune checkpoint inhibitor response</li><li>• Personalized cancer immunotherapy</li></ul>
  </article>
  <article class="app-card" style="left:429px">
    <h3 style="margin-left:0">Autoimmunity</h3>
    <ul><li>• Autoimmune disease profiling</li><li>• Treatment response monitoring</li><li>• Biomarker discovery</li><li>• Therapeutic target identification</li></ul>
  </article>
  <article class="app-card" style="left:800px">
    <h3 style="margin-left:0">Research</h3>
    <ul><li>• Vaccine development</li><li>• Immunological studies</li><li>• Drug discovery screening</li><li>• Academic research applications</li></ul>
  </article>
</section>

<section>
  <div class="abs contact-band"></div>
  <div class="abs contact-card"></div>
  <h2 class="abs heading contact-title">Contact Us</h2>
  <p class="abs contact-text">Ready to revolutionize your research? Let's discuss <span class="swash">how VORENT can</span> accelerate your discoveries</p>
  <div class="abs social" aria-label="Social media links"><i></i><i></i></div>
  <div class="info" style="top:3816px"><b>Phone</b><span>(555) 014-2290</span></div>
  <div class="info" style="top:3905px"><b>Email</b><span>hello@vorentbio-lab.com</span></div>
  <div class="abs contact-art" role="img" aria-label="Watercolour illustration of a doctor in a white coat attending to a seated patient in a green dress"></div>
  <p class="abs caption">We are an accessible workplace.<br>Persons with disabilities are welcome to apply.</p>
</section>

</body>
</html>
```